Business Card Design

It's an investment advisory service for individuals with all there investment needs. Also financial consulting to businesses and governmental agencies on retirement plans etc. It's personalized not commoditized help. Should show strength, knowledge and money orientation.
Updates

Reason: Will be out of town setting up office.

Reason: waiting for the 2/3rds of group to vote

Reason: only half the votes are in, I'm calling and getting verbals, but at this time we are down to 2 designs.

Industry/Entity Type

Investment

Contact Information for Business Card

B. Rel K. Financial Consulting and Wealth Management, Desmond Wick Harlow, 5172 Paseo Loma Verde Crest, San Diego, CA 92131-4817, Registered Investment Advisor

Requirements
Nice to have
• Something money oriented

```html
<!DOCTYPE html>
<html lang="en">
<head>
<meta charset="utf-8">
<title>B. Rel K. Financial Consulting – Business Card</title>
<link rel="stylesheet" href="https://fonts.googleapis.com/css2?family=Lato:wght@400;700;900&family=Mulish:wght@800&display=swap">
<style>
  :root {
    --backdrop: #e9e6e1;
    --card-blue: #0b57ae;
    --band-yellow: #fdf69a;
    --rule-white: #ffffff;
    --name-yellow: #fdf27a;
    --ink-dark: #111111;
    --text-light: #e8eef8;
    --text-muted: #c3cfe2;
  }
  * { box-sizing: border-box; margin: 0; padding: 0; }
  html, body {
    width: 1200px;
    height: 900px;
    overflow: hidden;
    background: var(--backdrop);
  }
  .canvas {
    width: 1200px;
    height: 900px;
    display: flex;
    align-items: center;
    justify-content: center;
  }
  .business-card {
    position: relative;
    width: 1000px;
    height: 572px;
    background: var(--card-blue);
    overflow: hidden;
    box-shadow: 0 6px 24px rgba(0,0,0,0.18);
  }
  .advisor-name {
    position: absolute;
    right: 48px;
    top: 62px;
    font-family: "Lato", sans-serif;
    font-weight: 900;
    font-size: 48px;
    color: var(--name-yellow);
    letter-spacing: 0.3px;
  }
  .rule {
    position: absolute;
    left: 0;
    width: 100%;
    height: 6px;
    background: var(--rule-white);
  }
  .rule--top { top: 132px; }
  .rule--bottom { top: 284px; }
  .firm-band {
    position: absolute;
    left: 0;
    top: 148px;
    width: 100%;
    height: 126px;
    background: var(--band-yellow);
    display: flex;
    flex-direction: column;
    justify-content: center;
    padding-left: 200px;
    font-family: "Mulish", sans-serif;
    font-weight: 800;
    font-size: 40px;
    line-height: 1.1;
    color: var(--ink-dark);
  }
  .firm-band .firm-line--second { padding-left: 30px; }
  .credential {
    position: absolute;
    left: 300px;
    top: 312px;
    font-family: "Lato", sans-serif;
    font-weight: 400;
    font-size: 32px;
    color: var(--text-light);
  }
  .address {
    position: absolute;
    left: 44px;
    top: 388px;
    display: flex;
    gap: 12px;
    font-family: "Lato", sans-serif;
    font-size: 26px;
    line-height: 1.25;
    color: var(--text-muted);
  }
  .address svg { margin-top: 4px; flex: none; }
  .postal {
    position: absolute;
    left: 560px;
    top: 470px;
    display: flex;
    align-items: center;
    gap: 22px;
    font-family: "Lato", sans-serif;
    font-size: 30px;
    color: var(--text-muted);
  }
</style>
</head>
<body>
  <main class="canvas">
    <section class="business-card">
      <h1 class="advisor-name">Desmond Wick Harlow</h1>
      <div class="rule rule--top"></div>
      <div class="firm-band">
        <span class="firm-line">B. Rel K. Financial Consulting</span>
        <span class="firm-line firm-line--second">and Wealth Management</span>
      </div>
      <div class="rule rule--bottom"></div>
      <p class="credential">Registered Investment Advisor</p>
      <div class="address">
        <svg width="18" height="24" viewBox="0 0 18 24" aria-hidden="true">
          <path d="M9 0C4 0 0 4 0 9c0 6.5 9 15 9 15s9-8.5 9-15C18 4 14 0 9 0z" fill="var(--text-muted)"/>
          <circle cx="9" cy="9" r="3.5" fill="var(--card-blue)"/>
        </svg>
        <div>
          <div>5172 Paseo Loma Verde Crest,</div>
          <div>San Diego, CA</div>
        </div>
      </div>
      <div class="postal">
        <svg width="22" height="26" viewBox="0 0 22 26" aria-hidden="true">
          <path d="M5 1l4 6-3 3c1.5 4 4 7 8 9l3-3 5 4-3 5C9 24 0 14 1 4z" fill="var(--text-muted)"/>
        </svg>
        <span>92131-4817,</span>
      </div>
    </section>
  </main>
</body>
</html>
```